Website for Fernvale Harmony Chapel

Wordpress website design required for Fernvale Harmony Chapel. We are a family oriented church catering for age groups from school age to elderly people. The church has a wide variety of activities which it coordinates. The idea is to describe the activities on the activities page, but cross-link them to show which would be applicable to the different age groups.

We would like an inviting website which is easy to read and navigate.

Target Market(s)

Very wide audience - from school age youth to elderly people, so design and style should cater for both audiences.

Industry/Entity Type

Church

Coding

Coded - Design and coding required

Number of Pages Required

5+ page

Font styles to use
Sans Serif

Colors
0255a3
ffffff
0792cd
f78f20

Requirements
Must have
• Inviting website.
• Clear readable font.
• Space to import photos to balance text on each page.
• Need to project a dynamic and progressive feel for the church.
• Easy to navigate.
Nice to have
• Scrolling photos on pages. Ability to enter questions/ comments/prayer requests on Home page.
Should not have
• Conservative audience, so should not be too bold.

```html
<!DOCTYPE html>
<html lang="en">
<head>
<meta charset="utf-8">
<title>Fernvale Harmony Chapel</title>
<link rel="stylesheet" href="https://fonts.googleapis.com/css2?family=Open+Sans:wght@400;600;700;800&family=Lora:ital,wght@1,400;1,700&display=swap">
<style>
:root{
  --navy:#0255a3;
  --blue:#0792cd;
  --orange:#f78f20;
  --white:#ffffff;
  --ink:#2e2e2e;
  --grey:#6b6b6b;
  --rule:#9a9a9a;
  --sand:#efe9dd;
  --night:#1d2330;
  --serif:'Lora', Georgia, serif;
  --sans:'Open Sans', Arial, sans-serif;
}
*{box-sizing:border-box;margin:0;padding:0}
html,body{width:1200px;height:4100px;overflow:hidden}
body{font-family:var(--sans);color:var(--ink);background:var(--white);position:relative}
section,header,footer{position:absolute;left:0;width:1200px}
.abs{position:absolute}
.btn{position:absolute;display:flex;align-items:center;justify-content:center;background:var(--orange);color:var(--white);font:700 14px var(--sans);letter-spacing:.5px;text-transform:uppercase;text-decoration:none}
.script{font-family:var(--serif);font-style:italic}
.rule{position:absolute;height:1px;background:var(--rule)}
.rule.light{background:rgba(255,255,255,.85)}

/* hero */
.hero{top:0;height:601px;overflow:hidden}
.hero-photo{position:absolute;inset:0;background:linear-gradient(180deg,#d9e0e4 0%,#e9e7df 45%,#ddd6c6 80%,#cfc6b1 100%)}
.hero-photo::after{content:"";position:absolute;left:640px;top:60px;width:480px;height:460px;background:radial-gradient(ellipse at center,rgba(160,170,175,.45),rgba(160,170,175,0) 70%)}
.nav{position:absolute;left:49px;top:27px;width:1099px;height:96px;background:var(--white);box-shadow:0 2px 6px rgba(0,0,0,.12);font-size:14px;color:#444}
.nav a{position:absolute;top:38px;color:#444;text-decoration:none}
.brand{position:absolute;left:420px;width:260px;top:22px;text-align:center}
.brand-mark{display:inline-block;width:18px;height:18px;border-radius:50%;background:var(--orange);vertical-align:middle;margin-right:6px}
.brand-name{font:600 14px var(--sans);color:var(--navy);vertical-align:middle}
.brand-tag{display:block;font:400 10px var(--sans);color:var(--grey);margin-top:6px;letter-spacing:1px}
.hero-kicker{position:absolute;top:244px;width:1200px;text-align:center;font-size:22px;color:#7a7a7a}
.hero-title{position:absolute;top:262px;width:1200px;text-align:center;font:700 98px/1.1 var(--sans);color:var(--blue)}
.hero-tagline{position:absolute;top:392px;width:1200px;text-align:center;font-size:32px;color:#666}

/* event */
.event{top:601px;height:159px;background:var(--sand)}
.event-label{position:absolute;left:120px;top:52px;font:700 14px var(--sans);color:#555;letter-spacing:.5px}
.event-title{position:absolute;left:120px;top:72px;font-size:24px;color:#555}
.count{position:absolute;top:49px;width:64px;height:69px;border:2px solid var(--rule);background:var(--white);text-align:center}
.count b{display:block;font:700 30px/46px var(--sans);color:#555}
.count span{display:block;border-top:2px solid var(--rule);font:600 10px/19px var(--sans);color:#666;text-transform:uppercase}
.event-or{position:absolute;left:906px;top:70px;font-size:14px;color:#666}
.btn-outline{position:absolute;display:flex;align-items:center;justify-content:center;border:2px solid var(--orange);color:#555;font:700 12px var(--sans);text-transform:uppercase;text-decoration:none}

/* welcome */
.welcome{top:760px;height:483px;background:var(--white)}
.welcome-label{position:absolute;top:80px;width:1200px;text-align:center;font:700 14px var(--sans);color:#555;letter-spacing:.5px}
.welcome-name{position:absolute;top:100px;width:1200px;text-align:center;font-size:22px;color:#666}
.col-title{position:absolute;top:172px;font:700 14px var(--sans);color:#444}
.col-text{position:absolute;top:194px;width:490px;font-size:12.5px;line-height:20px;color:#555}

/* activities */
.activities{top:1243px;height:547px;background:linear-gradient(180deg,#1c8fcd 0%,#2b9fd7 40%,#1a86c4 100%);overflow:hidden}
.section-title{position:absolute;width:1200px;text-align:center;font-size:26px;color:var(--white)}
.strip{position:absolute;top:164px;left:0;width:1200px;height:211px;display:flex}
.strip .photo{flex:1}
.activity-card{flex:1;background:#f3f3f3;position:relative}
.activity-card .frame{position:absolute;left:24px;top:18px;right:24px;bottom:18px;border:3px solid var(--orange);display:flex;flex-direction:column;align-items:center;justify-content:center}
.activity-card .frame b{font:700 13px var(--sans);color:#777;letter-spacing:.5px}
.dots{position:absolute;top:388px;left:580px;display:flex;gap:6px}
.dots i{width:9px;height:9px;border-radius:50%;background:rgba(255,255,255,.6)}
.dots i:first-child{background:var(--white)}

/* sermons & news */
.sermons{top:1790px;height:710px;background:linear-gradient(180deg,#ecebe8 0%,#dedcd8 55%,#e9e7e3 100%)}
.sub-label{position:absolute;font:700 14px var(--sans);color:#444}
.sub-title{position:absolute;font-size:26px;color:#444}
.sermon{position:absolute;left:120px;width:418px;height:44px;background:var(--white);display:flex;align-items:center;font-size:14px;color:#333;box-shadow:0 1px 2px rgba(0,0,0,.08)}
.sermon .mic{width:44px;height:44px;background:var(--orange);display:flex;align-items:center;justify-content:center;margin-right:14px;flex:none}
.sermon.active{background:var(--blue);color:var(--white);font-weight:700}
.sermon.active .mic{background:var(--navy)}
.sermon-detail{position:absolute;left:120px;top:276px;width:418px;height:160px;background:var(--white);padding:12px 18px;font-size:11.5px;line-height:17px;color:#555}
.sermon-meta{display:flex;gap:26px;font:600 10px var(--sans);text-transform:uppercase;color:#555;margin-bottom:10px}
.sermon-foot{display:flex;justify-content:space-between;margin-top:14px;font:600 10px var(--sans);text-transform:uppercase;color:#444}
.news{position:absolute;left:598px;width:465px;height:96px;background:var(--white);border-bottom:6px solid var(--orange);display:flex}
.news .thumb{width:90px;height:90px;flex:none;background:linear-gradient(135deg,#cfd3d6,#eceeef)}
.news .body{padding:12px 14px}
.news h4{font:400 15px/20px var(--serif);color:#333}
.news p{font-size:11px;color:var(--orange);font-weight:600;margin-top:4px}
.news p.plain{color:#666;font-weight:400}

/* prayer */
.prayer{top:2500px;height:506px;background:linear-gradient(180deg,#0f8fd0 0%,#1b9ad6 50%,#0b7cbf 100%)}
.prayer-intro{position:absolute;top:140px;left:150px;width:900px;text-align:center;font:italic 700 13px/20px var(--serif);color:var(--white)}
.field{position:absolute;background:var(--white);font:italic 14px var(--serif);color:#777;padding:8px 14px}

/* minister */
.minister{top:3006px;height:765px;background:linear-gradient(180deg,#f3f2ef 0%,#ebe9e4 100%)}
.minister-photo{position:absolute;left:109px;top:69px;width:438px;height:696px;background:linear-gradient(180deg,#d9d6cf 0%,#2c2a2b 35%,#1e1d1f 100%);border-radius:200px 200px 0 0}
.msg-label{position:absolute;left:560px;width:520px;top:148px;text-align:center;font-size:22px;color:#777}
.quote{position:absolute;left:580px;width:480px;top:200px;text-align:center;font:italic 400 29px/38px var(--serif);color:var(--orange)}
.msg-body{position:absolute;left:590px;width:460px;top:334px;text-align:center;font:700 12px/18px var(--sans);color:#666;text-transform:uppercase}
.msg-sign{position:absolute;left:560px;width:520px;top:430px;text-align:center;font:700 14px var(--sans);color:#777}
.msg-more{position:absolute;left:760px;width:120px;top:486px;text-align:center;font:700 12px var(--sans);color:#fff;background:rgba(255,255,255,.35);padding:4px 0;text-transform:uppercase}

/* footer */
.footer{top:3651px;height:449px;background:linear-gradient(180deg,rgba(29,35,48,0) 0%,#2a3241 22%,var(--night) 30%,#141820 100%)}
.foot-title{position:absolute;top:142px;font:700 22px var(--sans);color:var(--white)}
.foot-text{position:absolute;font:700 13px/19px var(--sans);color:var(--white)}
.foot-text.orange{color:var(--orange)}
.foot-list{position:absolute;top:196px;list-style:none;font:700 13px/20px var(--sans);color:var(--white)}
.social{position:absolute;top:352px;left:120px;display:flex;gap:12px}
.social i{width:12px;height:12px;border-radius:50%;background:var(--white)}
.badge{position:absolute;left:812px;top:142px;width:248px;height:211px;background:var(--white);outline:4px solid var(--white);border:2px solid #333;display:flex;flex-direction:column;align-items:center;padding-top:30px}
.badge .dot{width:44px;height:44px;border-radius:50%;background:var(--night)}
.badge small{font-size:10px;color:#444;margin-top:12px}
.badge b{font:700 22px var(--sans);color:#333;letter-spacing:1px}
.badge .badge-btn{margin-top:10px;background:var(--orange);color:var(--white);font:700 11px var(--sans);padding:6px 24px;text-transform:uppercase}
.copy-rule{position:absolute;left:120px;width:943px;top:404px;border-top:1px dashed rgba(255,255,255,.4)}
.copy{position:absolute;top:415px;width:1200px;text-align:center;font-size:12px;color:#999}
.copy b{color:var(--white)}
</style>
</head>
<body>

<header class="hero">
  <div class="hero-photo" role="img" aria-label="Soft sky scene with an open-armed figure and doves in flight"></div>
  <nav class="nav">
    <a style="left:78px">Home</a>
    <a style="left:160px">Age Group</a>
    <a style="left:262px">Activities</a>
    <div class="brand">
      <span class="brand-mark"></span><span class="brand-name">Fernvale Harmony Chapel</span>
      <span class="brand-tag">A family of faith</span>
    </div>
    <a style="left:760px">Events</a>
    <a style="left:858px">About FHC</a>
    <a style="left:968px">Contact</a>
  </nav>
  <div class="hero-kicker script">Building Holy and Healthy Lives</div>
  <h1 class="hero-title">The Family</h1>
  <div class="rule" style="left:530px;top:380px;width:140px"></div>
  <div class="hero-tagline script">Love, Care, Share</div>
  <a class="btn" style="left:538px;top:470px;width:200px;height:41px">Learn More</a>
</header>

<section class="event">
  <div class="event-label">UPCOMING EVENT</div>
  <div class="event-title script">Art lessons for children</div>
  <div class="count" style="left:445px"><b>05</b><span>Days</span></div>
  <div class="count" style="left:525px"><b>20</b><span>Hours</span></div>
  <div class="count" style="left:605px"><b>25</b><span>Minutes</span></div>
  <div class="count" style="left:686px"><b>52</b><span>Seconds</span></div>
  <a class="btn" style="left:810px;top:64px;width:86px;height:36px;font-size:12px">Join Now</a>
  <span class="event-or">or</span>
  <a class="btn-outline" style="left:935px;top:64px;width:128px;height:36px">View More Event</a>
</section>

<section class="welcome">
  <div class="welcome-label">WELCOME TO THE</div>
  <div class="welcome-name script">Fernvale Harmony Chapel</div>
  <div class="rule" style="left:545px;top:142px;width:110px"></div>
  <div class="col-title" style="left:120px">ABOUT US</div>
  <p class="col-text" style="left:120px">Lorem ipsum dolor sit amet, consectetur adipiscing elit. Aenean ut massa non lacus vehicula tristique quis sit amet nulla. Nullam vestibulum mi porttitor nisi tempus fermentum. Nam pellentesque lacinia mattis. Etiam vehicula mi sed libero dapibus, a porta erat facilisis. In non vestibulum justo, ut sollicitudin tellus. Aenean at tincidunt lacus. Vestibulum sit amet sagittis lorem. Suspendisse lectus elit, molestique eget nisl nec, suscipit hendrerit urna. Donec at eros ex.</p>
  <a class="btn" style="left:120px;top:355px;width:164px;height:42px">Read More</a>
  <div class="col-title" style="left:612px">OUR MISSION</div>
  <p class="col-text" style="left:612px">Lorem ipsum dolor sit amet, consectetur adipiscing elit. Aenean ut massa non lacus vehicula tristique quis sit amet nulla. Nullam vestibulum mi porttitor nisi tempus fermentum. Nam pellentesque lacinia mattis. Etiam vehicula mi sed libero dapibus, a porta erat facilisis. In non vestibulum justo, ut sollicitudin tellus. Aenean at tincidunt lacus. Vestibulum sit amet sagittis lorem. Suspendisse lectus elit, molestique eget nisl nec, suscipit hendrerit urna. Donec at eros ex.</p>
  <a class="btn" style="left:612px;top:355px;width:164px;height:42px">Read More</a>
</section>

<section class="activities">
  <div class="section-title script" style="top:76px">Recent Activities</div>
  <div class="rule light" style="left:545px;top:120px;width:110px"></div>
  <div class="strip">
    <div class="photo" role="img" aria-label="Children gathered at a red-draped altar table" style="background:linear-gradient(135deg,#8c2a28,#c8574a 60%,#e7d8cc)"></div>
    <div class="activity-card">
      <div class="frame">
        <b>NAME OF THE ACTIVITY</b>
        <svg width="30" height="30" viewBox="0 0 30 30" style="margin-top:16px"><circle cx="13" cy="13" r="8" stroke="#f78f20" stroke-width="3" fill="none"/><line x1="19" y1="19" x2="26" y2="26" stroke="#f78f20" stroke-width="3"/><line x1="13" y1="9" x2="13" y2="17" stroke="#f78f20" stroke-width="2"/><line x1="9" y1="13" x2="17" y2="13" stroke="#f78f20" stroke-width="2"/></svg>
      </div>
    </div>
    <div class="photo" role="img" aria-label="Group of children in a classroom activity" style="background:linear-gradient(135deg,#6c4a3e,#b9776a 55%,#d7b9a6)"></div>
    <div class="photo" role="img" aria-label="Young group dressed for a nativity play" style="background:linear-gradient(135deg,#5a3b32,#9c6a54 55%,#c9a88f)"></div>
  </div>
  <div class="dots"><i></i><i></i><i></i></div>
  <a class="btn" style="left:481px;top:427px;width:241px;height:41px">View All Activities</a>
</section>

<section class="sermons">
  <div class="sub-label" style="left:120px;top:78px">OUR</div>
  <div class="sub-title script" style="left:120px;top:96px">Latest Sermons</div>
  <div class="rule" style="left:120px;top:140px;width:130px"></div>

  <div class="sermon" style="top:178px"><span class="mic"><svg width="14" height="22" viewBox="0 0 14 22"><rect x="3" y="0" width="8" height="13" rx="4" fill="#fff"/><path d="M1 10 a6 6 0 0 0 12 0" stroke="#fff" stroke-width="1.5" fill="none"/><line x1="7" y1="16" x2="7" y2="21" stroke="#fff" stroke-width="1.5"/></svg></span>Lorem ipsum dolor sit amet, consectetur adipi.</div>
  <div class="sermon active" style="top:230px"><span class="mic"><svg width="14" height="22" viewBox="0 0 14 22"><rect x="3" y="0" width="8" height="13" rx="4" fill="#fff"/><path d="M1 10 a6 6 0 0 0 12 0" stroke="#fff" stroke-width="1.5" fill="none"/><line x1="7" y1="16" x2="7" y2="21" stroke="#fff" stroke-width="1.5"/></svg></span>Lorem ipsum dolor sit amet, consectetur adipi.</div>
  <div class="sermon-detail">
    <div class="sermon-meta"><span>Category: Awe</span><span>Media: Speaker</span><span>Download</span></div>
    Lorem ipsum dolor sit amet, consectetur adipiscing elit. Duis euismod diam tellus, vel mattis ex consequat vel. Phasellus ut diam vel eros lobortis pharetra ut sit amet. Praesent vel enim. Lorem ipsum dolor sit amet, consectetur adipiscing elit.
    <div class="sermon-foot"><span>&#9654; &#9660; &#8942;</span><span>Share This Sermon</span></div>
  </div>
  <div class="sermon" style="top:446px"><span class="mic"><svg width="14" height="22" viewBox="0 0 14 22"><rect x="3" y="0" width="8" height="13" rx="4" fill="#fff"/><path d="M1 10 a6 6 0 0 0 12 0" stroke="#fff" stroke-width="1.5" fill="none"/><line x1="7" y1="16" x2="7" y2="21" stroke="#fff" stroke-width="1.5"/></svg></span>Lorem ipsum dolor sit amet, consectetur adipi.</div>
  <div class="sermon" style="top:495px"><span class="mic"><svg width="14" height="22" viewBox="0 0 14 22"><rect x="3" y="0" width="8" height="13" rx="4" fill="#fff"/><path d="M1 10 a6 6 0 0 0 12 0" stroke="#fff" stroke-width="1.5" fill="none"/><line x1="7" y1="16" x2="7" y2="21" stroke="#fff" stroke-width="1.5"/></svg></span>Lorem ipsum dolor sit amet, consectetur adipi.</div>
  <div class="sermon" style="top:544px"><span class="mic"><svg width="14" height="22" viewBox="0 0 14 22"><rect x="3" y="0" width="8" height="13" rx="4" fill="#fff"/><path d="M1 10 a6 6 0 0 0 12 0" stroke="#fff" stroke-width="1.5" fill="none"/><line x1="7" y1="16" x2="7" y2="21" stroke="#fff" stroke-width="1.5"/></svg></span>Lorem ipsum dolor sit amet, consectetur adipi.</div>

  <div class="sub-label" style="left:598px;top:78px">LATEST</div>
  <div class="sub-title script" style="left:598px;top:96px">News &amp; Updates</div>
  <div class="rule" style="left:598px;top:140px;width:130px"></div>

  <div class="news" style="top:172px"><div class="thumb" role="img" aria-label="Pale decorative pattern"></div><div class="body"><h4>Blessed are all those who take refuge in him!</h4><p>By Admin &middot; May 12 2017</p></div></div>
  <div class="news" style="top:288px"><div class="thumb" role="img" aria-label="Church window light" style="background:linear-gradient(135deg,#b9c2c7,#e6e8e9)"></div><div class="body"><h4>Love the Lord, Your God with All Your heart &amp; He Shall Response!</h4><p>By Admin &middot; May 12 2017</p></div></div>
  <div class="news" style="top:400px"><div class="thumb" role="img" aria-label="Open bible on a table" style="background:linear-gradient(135deg,#d9d1c2,#f1ede6)"></div><div class="body"><h4>Reading of the Bible</h4><p class="plain">Blessed is the man who does not walk in the counsel of the wicked.</p></div></div>
  <div class="news" style="top:512px"><div class="thumb" role="img" aria-label="Hands folded in prayer" style="background:linear-gradient(135deg,#9aa4ab,#d8dcdf)"></div><div class="body"><h4>Where Then Is My Hope &amp; Who Can See Any Hope For Me?</h4></div></div>
</section>

<section class="prayer">
  <div class="section-title script" style="top:76px">Prayer Request Or Ask Questions</div>
  <div class="rule light" style="left:545px;top:120px;width:110px"></div>
  <p class="prayer-intro">Lorem ipsum dolor sit amet, consectetur adipiscing elit. Aenean ut massa non lacus vehicula tristique quis sit amet nulla. Nullam vestibulum mi porttitor nisi tempus fermentum.</p>
  <div class="field" style="left:303px;top:211px;width:292px;height:41px">Name</div>
  <div class="field" style="left:604px;top:211px;width:292px;height:41px">Contact Number</div>
  <div class="field" style="left:303px;top:263px;width:593px;height:40px">Your Email</div>
  <div class="field" style="left:303px;top:312px;width:593px;height:56px">Message</div>
  <a class="btn" style="left:508px;top:400px;width:186px;height:41px">Request Now</a>
</section>

<section class="minister">
  <div class="minister-photo" role="img" aria-label="Portrait of the minister in robes holding an open bible"></div>
  <div class="msg-label script">Minister's weekly message</div>
  <div class="rule" style="left:765px;top:186px;width:110px"></div>
  <div class="quote">&ldquo;God has given us two hands, one to receive with and the other to give with.&rdquo;</div>
  <p class="msg-body">Lorem ipsum dolor sit amet, consectetur adipiscing elit. Duis euismod diam tellus, vel mattis ex consequat vel. Phasellus ut diam vel eros.</p>
  <div class="msg-sign">- R. Calder</div>
  <div class="msg-more">Read More</div>
</section>

<footer class="footer">
  <div class="abs" role="img" aria-label="Silhouette of a forest treeline with birds" style="left:0;top:0;width:1200px;height:110px;background:linear-gradient(180deg,rgba(60,70,85,0) 0%,rgba(40,48,62,.85) 100%)"></div>
  <div class="foot-title" style="left:120px">CONTACT</div>
  <p class="foot-text" style="left:120px;top:196px;width:220px">Lorem ipsum dolor sit amet, con sectetur adipiscing elit. Vestibu lum vitae lobortis lacus.</p>
  <div class="foot-text" style="left:120px;top:278px"><svg width="14" height="14" viewBox="0 0 14 14" style="vertical-align:-2px;margin-right:8px"><path d="M3 1 l3 3 -2 2 q1 3 4 4 l2 -2 3 3 -2 2 q-8 -1 -10 -10z" fill="#fff"/></svg>555-014-2290</div>
  <div class="foot-text" style="left:120px;top:310px"><svg width="14" height="12" viewBox="0 0 14 12" style="vertical-align:-1px;margin-right:8px"><rect x="0" y="0" width="14" height="12" fill="#fff"/><path d="M0 0 l7 6 7 -6" stroke="#1d2330" fill="none"/></svg>info@fernvalechapel.org</div>
  <div class="social"><i></i><i></i></div>

  <div class="foot-title" style="left:402px">QUICK LINK</div>
  <ul class="foot-list" style="left:402px">
    <li>Home</li><li>Age Group</li><li>Activities</li><li>Events</li><li>About FHC</li><li>Contact</li>
  </ul>

  <div class="foot-title" style="left:598px">SERVICE TIMES</div>
  <div class="foot-text" style="left:598px;top:196px">Monday to Friday</div>
  <div class="foot-text orange" style="left:598px;top:216px">10:00am to 6:00pm</div>
  <div class="foot-text" style="left:598px;top:250px">Sunday to Saturday</div>
  <div class="foot-text orange" style="left:598px;top:270px">9:00am to 6:00pm</div>

  <div class="badge">
    <span class="dot"></span>
    <small>Proud to be a part of</small>
    <b>HARMONY CHAPEL</b>
    <span class="badge-btn">Click here for more</span>
  </div>

  <div class="copy-rule"></div>
  <div class="copy">Copyright 2016 <b>Fernvale Harmony Chapel</b>. All Rights Reserved</div>
</footer>

</body>
</html>
```